Need a clean & modern homepage for an education site + opportunity for longer term work

Thanks for viewing our project. We are excited about this new website and we hope that we might build a relationship with designers as we work on this project. I provided quite a few details and requirements to help you more quickly create a design that meets our needs.
Who we are:
We are a website that discusses the importance of college accreditation and provides a directory of college programs.
What we need:
A homepage that meets the below requirements and is inspired by the examples provided
Definition of accredited:
ac·cred·it·ed [uh-kred-i-tid] adj.
1. officially recognized as meeting the essential requirements, as of academic excellence: accredited schools.
2. provided with official credentials, as by a government: an accredited diplomatic representative.
3. accepted as authoritative: an accredited theory.
Overall look and feel for the homepage:
- Clean, simple and modern
- Limited (or zero) pictures
- Utilize color blocks with text
- A trend seems to be longer vertical length homepages with lots of whitespace. I generally like this trend as long as the page is not way to tall.
Inspirations: Sites that have a similar look and feel to what I need.
http://plinvar.org/
http://www.tumbrelstat.com/colleges/harrowgate-university/
http://quietmarble.org/
http://www.vellichorstaffing.com/
http://www.plonk.com/
http://sketches.zimvo.com/
Items to be included on the homepage. Details below on each item.
- Top navigation
- Logo: Please leave a blank area for a logo. The logo has not been designed.
- Simple graphic/color block at the top that highlights a definition of “Accredited” – the definition should be formatted like it is being copy/pasted from a dictionary.
- Space for a video and small (50 word) written description of the video. You can use placeholder text.
- One section with 3 Paragraphs of content (each paragraph around 100 words) with a header at the top. You can use placeholder text but please create the formatting. At the end of the 3 paragraphs please have a “Read More” Note this shouldn't be 3 separate paragraphs with three read mores - it is 3 paragraphs with one read more at the end.
- An area with the header “Search Colleges by State” that has anchor text links to all 50 states.
Top navigation:
- Home
- States – with a subnav dropdown that includes all 50 US states.
- Programs – with a subnav dropdown that includes program titles (list below)
- Degrees - with a subnav dropdown that includes 5 degree levels (list below)
- Accreditation – no subnav
- Rankings – no subnav
- Resources – no subnav
Footer
- Link to about us, privacy, and a copyright www.url.com
Programs List for sub navigation
Accounting
Art
Bible
Business
Criminal Justice
Design
Engineering
English
Law
LPN to RN
Management
Math
MBA
MPH
Medical Assisting
Military
Nursing
Occupational Therapy
Paralegal
Psychology
Pharmacy
RN to BSN
Radiology
Social Work
Sonography
Degrees list for sub navigation
Certificate
Associate
Bachelors
Masters
PhD
Thanks so much - looking forward to working with you!

```html
<!DOCTYPE html>
<html lang="en">
<head>
<meta charset="utf-8">
<title>Accredited Colleges – Home</title>
<link rel="stylesheet" href="https://fonts.googleapis.com/css2?family=Montserrat:wght@400;500;600;700&family=Merriweather+Sans:wght@300;400;700&family=Signika:wght@600&display=swap">
<style>
  :root {
    --teal: #56a9b6;
    --teal-bar: #55a7b5;
    --teal-dark: #2a93a2;
    --teal-active: #3f97a5;
    --teal-deep: #2f6f7a;
    --line: #6fb6c2;
    --panel: #f2f6fa;
    --white: #ffffff;
    --muted: #e1f1f4;
    --grey-text: #8c8f93;
    --select-border: #e3e7ea;
    --sketch-bg: #eef0f7;
  }
  * { box-sizing: border-box; margin: 0; padding: 0; }
  html, body { width: 1200px; height: 1000px; overflow: hidden; background: var(--white); }
  body { position: relative; font-family: "Merriweather Sans", sans-serif; }

  .utility-bar { position: absolute; left: 0; top: 0; width: 1200px; height: 35px; background: var(--teal-bar); border-bottom: 1px solid var(--line); }
  .utility-links { position: absolute; right: 166px; top: 0; height: 35px; display: flex; align-items: center; font-family: "Montserrat", sans-serif; font-size: 11px; color: var(--muted); }
  .utility-links span { padding: 0 10px; border-left: 1px solid var(--line); line-height: 24px; }
  .utility-links span:first-child { border-left: none; }
  .social { display: flex; gap: 9px; margin-left: 4px; }
  .social i { display: block; width: 15px; height: 15px; border-radius: 50%; background: #a9d3da; }

  .main-nav { position: absolute; left: 0; top: 35px; width: 1200px; height: 59px; background: var(--teal-bar); }
  .brand { position: absolute; left: 164px; top: 12px; font-family: "Montserrat", sans-serif; font-size: 31px; font-weight: 400; color: #e8f4f6; letter-spacing: -1px; }
  .nav-list { position: absolute; left: 340px; top: 13px; display: flex; list-style: none; font-family: "Montserrat", sans-serif; font-size: 13px; font-weight: 500; color: var(--white); }
  .nav-list li { padding: 15px 17px 15px; line-height: 16px; }
  .nav-list li.active { background: var(--teal-active); }

  .definition { position: absolute; left: 164px; top: 128px; width: 370px; height: 325px; background: var(--teal-dark); color: var(--white); padding: 22px 26px; }
  .definition h1 { font-family: "Montserrat", sans-serif; font-size: 25px; font-weight: 600; letter-spacing: -1px; line-height: 30px; }
  .definition .pos { font-family: "Montserrat", sans-serif; font-size: 18px; font-weight: 600; margin-top: 2px; }
  .senses { list-style: none; margin-top: 20px; }
  .senses li { display: flex; align-items: center; margin-bottom: 18px; }
  .senses .num { width: 36px; font-family: "Montserrat", sans-serif; font-size: 40px; font-weight: 400; line-height: 40px; }
  .senses p { font-size: 13.5px; line-height: 18px; font-weight: 300; }

  .sketch { position: absolute; left: 565px; top: 128px; width: 465px; height: 317px; background: radial-gradient(ellipse at center, var(--sketch-bg) 0%, var(--white) 75%); }

  .search { position: absolute; left: 0; top: 491px; width: 1200px; height: 149px; background: var(--panel); border-bottom: 3px solid #dfe4e8; }
  .search-notch { position: absolute; left: 586px; top: 0; width: 0; height: 0; border-left: 16px solid transparent; border-right: 16px solid transparent; border-top: 18px solid var(--white); }
  .search-title { position: absolute; left: 176px; top: 16px; display: flex; align-items: center; gap: 12px; font-family: "Montserrat", sans-serif; font-size: 22px; font-weight: 400; color: var(--teal-dark); }
  .select { position: absolute; top: 62px; height: 53px; background: var(--white); border: 3px solid var(--select-border); font-family: "Merriweather Sans", sans-serif; font-size: 13px; color: var(--grey-text); padding: 0 18px; display: flex; align-items: center; justify-content: space-between; }
  .select.state { left: 165px; width: 286px; }
  .select.college { left: 460px; width: 288px; }
  .select svg { margin-right: 2px; }
  .search-btn { position: absolute; left: 763px; top: 61px; width: 268px; height: 55px; background: var(--teal-dark); color: var(--white); font-family: "Signika", sans-serif; font-weight: 600; font-size: 18px; display: flex; align-items: center; justify-content: center; }

  .video-band { position: absolute; left: 0; top: 643px; width: 1200px; height: 332px; background: var(--teal); }
  .video { position: absolute; left: 166px; top: 52px; width: 429px; height: 217px; overflow: hidden; }
  .video-still { position: absolute; inset: 0; background: linear-gradient(100deg, #6b4a3c 0%, #b88f74 35%, #8a7a70 55%, #c04a52 80%, #5b3d34 100%); }
  .play { position: absolute; left: 171px; top: 44px; }
  .controls { position: absolute; left: 0; bottom: 0; width: 429px; height: 40px; background: rgba(10,20,25,.75); }
  .video-copy { position: absolute; left: 626px; top: 64px; width: 410px; color: var(--white); font-size: 15.3px; line-height: 22.7px; font-weight: 300; }
  .learn-more { position: absolute; left: 626px; top: 219px; display: flex; align-items: center; gap: 9px; font-family: "Signika", sans-serif; font-weight: 600; font-size: 16px; color: var(--white); }

  .footer { position: absolute; left: 0; top: 975px; width: 1200px; height: 25px; background: var(--teal-deep); }
</style>
</head>
<body>
  <header>
    <div class="utility-bar">
      <nav class="utility-links">
        <span>About</span><span>Contact</span><span>Keep Connected</span>
        <div class="social"><i></i><i></i><i></i></div>
      </nav>
    </div>
    <div class="main-nav">
      <div class="brand">LOGO</div>
      <ul class="nav-list">
        <li>HOME</li><li>STATES</li><li>PROGRAMS</li><li class="active">DEGREES</li><li>ACCREDITATION</li><li>RANKINGS</li><li>RESOURCES</li>
      </ul>
    </div>
  </header>

  <section class="definition">
    <h1>ac·cred·it·ed [uh-kred-i-tid]</h1>
    <div class="pos">adjective</div>
    <ol class="senses">
      <li><span class="num">1</span><p>officially recognized as meeting the essential requirements, as of academic excellence: accredited schools.</p></li>
      <li><span class="num">2</span><p>provided with official credentials, as by a government: an accredited diplomatic representative</p></li>
      <li><span class="num">3</span><p>accepted as authoritative: an accredited theory</p></li>
    </ol>
  </section>

  <div class="sketch" role="img" aria-label="Line sketch of a college building with binoculars and a graduation cap, captioned Find a college and Get accredited"></div>

  <section class="search">
    <div class="search-notch"></div>
    <h2 class="search-title">
      <svg width="34" height="34" viewBox="0 0 34 34"><circle cx="20" cy="13" r="9.5" fill="none" stroke="#2a93a2" stroke-width="3.5"/><line x1="13" y1="20" x2="4" y2="30" stroke="#2a93a2" stroke-width="5" stroke-linecap="round"/></svg>
      Search colleges by state
    </h2>
    <div class="select state">SELECT A STATE <svg width="28" height="16"><polygon points="0,0 28,0 14,16" fill="#2a93a2"/></svg></div>
    <div class="select college">SELECT A COLLEGE <svg width="28" height="16"><polygon points="0,0 28,0 14,16" fill="#2a93a2"/></svg></div>
    <div class="search-btn">SEARCH COLLEGE</div>
  </section>

  <section class="video-band">
    <div class="video">
      <div class="video-still" role="img" aria-label="Video still of a group of smiling students holding notebooks"></div>
      <svg class="play" width="90" height="90" viewBox="0 0 90 90"><circle cx="45" cy="45" r="42" fill="rgba(255,255,255,.12)" stroke="rgba(255,255,255,.7)" stroke-width="3"/><polygon points="36,30 36,60 60,45" fill="rgba(255,255,255,.75)"/></svg>
      <svg class="controls" width="429" height="40" viewBox="0 0 429 40">
        <polygon points="19,15 19,27 29,21" fill="#ffffff"/>
        <line x1="42" y1="21" x2="345" y2="21" stroke="#3a4a50" stroke-width="3"/>
        <line x1="42" y1="21" x2="76" y2="21" stroke="#56a9b6" stroke-width="3"/>
        <circle cx="76" cy="21" r="3" fill="#56a9b6"/>
        <rect x="362" y="18" width="3" height="6" fill="#ccc"/>
        <g fill="#ccc"><rect x="377" y="16" width="2" height="10"/><rect x="381" y="16" width="2" height="10"/><rect x="385" y="16" width="2" height="10"/><rect x="389" y="16" width="2" height="10"/></g>
        <rect x="402" y="16" width="14" height="10" fill="none" stroke="#ccc" stroke-width="1.5" stroke-dasharray="4 4"/>
      </svg>
    </div>
    <p class="video-copy">Lorem ipsum dolor sit amet, consectetur adipiscing elite Integer nec odio. Praesent libero. Sed cursus ante dapius diam. Sed nisi. Nulla quis sem at nibh entum imperdiet. Duis sagittis ipsum. Praesent mauris. Fusce nec tellus se augue semper porta. Mauris massa. Vestibulum lacinia arcu eget nulla. Class aptent taciti sociosq.</p>
    <div class="learn-more">
      <svg width="23" height="23" viewBox="0 0 23 23"><circle cx="11.5" cy="11.5" r="11.5" fill="#fff"/><path d="M5 9.5h6V5.5l7 6-7 6v-4H5z" fill="#56a9b6"/></svg>
      Learn more
    </div>
  </section>

  <footer class="footer"></footer>
</body>
</html>
```